Welcome Postcard for existing church in new facility

I need a postcard to express the 4 strong points of our ministry. I have attached a sample postcard that we really liked as a start point. Our four strengths are;

LOVE
WORSHIP
DIVERSITY
DOCTRINE

I want to make sure the colors used are vivid and provide plenty of pop.

I have provide images to coincide with the four ministry strengths and they are named according the the strength the coincide with, pick whichever you think is best graphically.

our twitter handle is @BHDAWNOK
our FB handle is /BHDAWNOK
our Youtube handle is /BrightHarbor

I must have all PSD layers in case last minutes changes need to be made. THIS IS A REQUIREMENT.

Target Market(s)

General Population

Industry/Entity Type

Non-Profit

Font styles to use
Sans Serif

Requirements
Must have
• I must have all PSD layers in case last minutes changes need to be made. THIS IS A REQUIREMENT.
Nice to have
• Be attractive and market friendly is US marketplace
Should not have
• Please do not submit multiple designs with slight deviations. If you submit multiple designs please make them totally different one from another. We will not consider your design if you spam us.

```html
<!DOCTYPE html>
<html lang="en">
<head>
<meta charset="UTF-8">
<title>Bright Harbor Ministries – Welcome Postcard</title>
<link rel="stylesheet" href="https://fonts.googleapis.com/css2?family=Bebas+Neue&family=EB+Garamond:wght@400&display=swap">
<style>
  :root {
    --paper: #ffffff;
    --brand-cyan: #1ec8f0;
    --brand-blue: #2a8fd8;
    --rule: #8a8a8a;
    --rule-dark: #555555;
    --frame: #7a7a7a;
    --tone-mid: #7b7b7b;
    --tone-light: #a9a9a9;
    --tone-dark: #5a5a5a;
    --love-a: #f04e6e;   --love-b: #f7a1b3;
    --worship-a: #7b5cd6; --worship-b: #b9a6f0;
    --diversity-a: #f5a623; --diversity-b: #f9d27e;
    --doctrine-a: #1f9fe0; --doctrine-b: #8fd4f5;
  }
  html, body {
    margin: 0;
    padding: 0;
    overflow: hidden;
    background: var(--paper);
  }
  .postcard {
    position: relative;
    width: 1200px;
    height: 783px;
    background: var(--paper);
    overflow: hidden;
  }
  .brand-mark {
    position: absolute;
    left: 30px;
    top: 42px;
    width: 180px;
    height: 180px;
    background: var(--brand-blue);
  }
  .brand-name {
    position: absolute;
    left: 328px;
    top: 100px;
    margin: 0;
    font-family: "EB Garamond", serif;
    font-weight: 400;
    font-size: 44px;
    line-height: 1;
    color: var(--brand-cyan);
  }
  .stamp-box {
    position: absolute;
    left: 935px;
    top: 26px;
    width: 231px;
    height: 229px;
    border: 1px solid var(--frame);
    box-sizing: border-box;
  }
  .address-line {
    position: absolute;
    left: 653px;
    width: 511px;
    height: 0;
    border-top: 1px solid var(--rule);
  }
  .address-line--1 { top: 451px; }
  .address-line--2 { top: 522px; }
  .address-line--3 { top: 582px; border-top-color: var(--rule-dark); }
  .address-line--4 { top: 654px; }

  .strength-gallery {
    position: absolute;
    left: 30px;
    top: 290px;
    width: 580px;
    height: 250px;
    display: grid;
    grid-template-columns: repeat(4, 1fr);
    gap: 12px;
  }
  .strength-photo { border-radius: 4px; }
  .strength-photo--love { background: linear-gradient(160deg, var(--love-a), var(--love-b)); }
  .strength-photo--worship { background: linear-gradient(160deg, var(--worship-a), var(--worship-b)); }
  .strength-photo--diversity { background: linear-gradient(160deg, var(--diversity-a), var(--diversity-b)); }
  .strength-photo--doctrine { background: linear-gradient(160deg, var(--doctrine-a), var(--doctrine-b)); }

  .social-handles {
    position: absolute;
    left: 30px;
    top: 600px;
    width: 580px;
    margin: 0;
    padding: 0;
    list-style: none;
    display: flex;
    justify-content: space-between;
    font-family: "Bebas Neue", sans-serif;
    font-size: 30px;
    line-height: 1;
    letter-spacing: 0.06em;
    color: var(--tone-dark);
  }

  .strengths {
    position: absolute;
    left: 8px;
    right: 8px;
    top: 716px;
    margin: 0;
    display: flex;
    justify-content: space-between;
    font-family: "Bebas Neue", sans-serif;
    font-size: 67px;
    line-height: 1;
    letter-spacing: 0.2em;
  }
  .strengths span:last-child { margin-right: -0.2em; }
  .strength--love { color: var(--tone-mid); }
  .strength--worship { color: var(--tone-light); }
  .strength--diversity { color: var(--tone-dark); }
  .strength--doctrine { color: var(--tone-light); }
</style>
</head>
<body>
  <main class="postcard">
    <div class="brand-mark" aria-hidden="true"></div>
    <h1 class="brand-name">Bright Harbor Ministries</h1>
    <div class="stamp-box" aria-label="Stamp area"></div>

    <section class="strength-gallery">
      <div class="strength-photo strength-photo--love" role="img" aria-label="Photo representing love"></div>
      <div class="strength-photo strength-photo--worship" role="img" aria-label="Photo representing worship"></div>
      <div class="strength-photo strength-photo--diversity" role="img" aria-label="Photo representing diversity"></div>
      <div class="strength-photo strength-photo--doctrine" role="img" aria-label="Photo representing doctrine"></div>
    </section>

    <ul class="social-handles">
      <li class="handle handle--twitter">@BHDAWNOK</li>
      <li class="handle handle--facebook">/BHDAWNOK</li>
      <li class="handle handle--youtube">/BrightHarbor</li>
    </ul>

    <div class="address-line address-line--1"></div>
    <div class="address-line address-line--2"></div>
    <div class="address-line address-line--3"></div>
    <div class="address-line address-line--4"></div>

    <p class="strengths">
      <span class="strength--love">Love</span>
      <span class="strength--worship">Worship</span>
      <span class="strength--diversity">Diversity</span>
      <span class="strength--doctrine">Doctrine</span>
    </p>
  </main>
</body>
</html>
```